Design the Keystone HR business card for my new business

I've just had a logo designed (attached) for my new business doing HR consulting. I'm a one person operation at this stage, my aim is to provide support and help to small to medium sized businesses with their people objectives or issues.

I'm not really into anything overly flashy, I'm not a PR or marketing agency. I'd like my card to look modern, professional and not gimmicky.

I'm thinking black front (to go with logo), double sided with details on the back, maybe in a different colour?

Logo attached in several different formats.

Front of the card to have logo and added text: People and Development Solutions

Back of the card to also feature logo in some way and say:
Megan Turlow
PO Box (TBA)
Marnoo Flats QLD 4381
0427 318 562
megan@keystonehr-example.com.au
www.keystonehr-example.com.au

Target Market(s)

Small to medium businesses / business owners.

Industry/Entity Type

Marketing

Requirements
Must have
• Double sided business card.
Should not have
• Anything overly gimmicky.

```html
<!DOCTYPE html>
<html lang="en">
<head>
<meta charset="utf-8">
<title>Keystone HR – Business Card</title>
<link rel="stylesheet" href="https://fonts.googleapis.com/css2?family=Questrial&display=swap">
<style>
  :root {
    --page-bg: #e9e6e1;
    --card-black: #0b0a0c;
    --card-edge: #1c1a1f;
    --white: #f4f4f6;
    --violet: #8a5bc4;
    --violet-soft: #6e4aa3;
    --grey: #9a979d;
    --shadow: rgba(0, 0, 0, 0.35);
  }
  * { box-sizing: border-box; margin: 0; padding: 0; }
  html, body {
    width: 1200px;
    height: 900px;
    overflow: hidden;
    background: var(--page-bg);
    font-family: "Questrial", "Century Gothic", sans-serif;
  }
  .canvas {
    position: relative;
    width: 1200px;
    height: 900px;
  }
  .card {
    position: absolute;
    width: 560px;
    height: 340px;
    border-radius: 16px;
    background: linear-gradient(160deg, var(--card-edge) 0%, var(--card-black) 45%);
    box-shadow: 0 10px 28px var(--shadow);
    color: var(--white);
  }
  .card--front { left: 70px; top: 60px; }
  .card--back { left: 570px; top: 500px; }

  /* Front */
  .brand-mark {
    position: absolute;
    left: 40px;
    top: 82px;
    width: 150px;
    height: 150px;
  }
  .brand-name {
    position: absolute;
    left: 205px;
    top: 118px;
    font-size: 62px;
    font-weight: 400;
    letter-spacing: -0.5px;
    line-height: 1;
    color: var(--white);
    white-space: nowrap;
  }
  .tagline {
    position: absolute;
    left: 150px;
    top: 236px;
    font-size: 15px;
    letter-spacing: 0.3px;
    text-transform: uppercase;
    color: var(--violet);
    white-space: nowrap;
  }

  /* Back */
  .email {
    position: absolute;
    left: 40px;
    top: 50px;
    font-size: 16px;
    letter-spacing: 2.4px;
    color: var(--violet);
    white-space: nowrap;
  }
  .back-mark {
    position: absolute;
    right: 34px;
    top: 36px;
    width: 96px;
    height: 96px;
  }
  .holder-name {
    position: absolute;
    left: 40px;
    top: 198px;
    font-size: 25px;
    letter-spacing: 0.5px;
    text-transform: uppercase;
    color: var(--white);
  }
  .rule {
    position: absolute;
    left: 40px;
    right: 40px;
    top: 236px;
    height: 2px;
    background: linear-gradient(90deg, var(--violet-soft), var(--violet) 60%, rgba(138, 91, 196, 0.5));
  }
  .address {
    position: absolute;
    left: 40px;
    top: 256px;
    font-style: normal;
    font-size: 14px;
    line-height: 1.45;
    color: var(--grey);
  }
</style>
</head>
<body>
<main class="canvas">

  <section class="card card--front" aria-label="Card front">
    <svg class="brand-mark" viewBox="0 0 150 150" aria-hidden="true">
      <circle cx="75" cy="75" r="70" fill="none" stroke="var(--violet)" stroke-width="3"/>
    </svg>
    <h1 class="brand-name">Keystone HR</h1>
    <p class="tagline">People and Development Solutions</p>
  </section>

  <section class="card card--back" aria-label="Card back">
    <p class="email">megan@keystonehr-example.com.au</p>
    <svg class="back-mark" viewBox="0 0 96 96" aria-hidden="true">
      <circle cx="48" cy="48" r="44" fill="none" stroke="var(--violet)" stroke-width="2.5"/>
    </svg>
    <h2 class="holder-name">Megan Turlow</h2>
    <div class="rule"></div>
    <address class="address">
      PO Box (TBA)<br>
      Marnoo Flats QLD 4381<br>
      0427 318 562
    </address>
  </section>

</main>
</body>
</html>
```